'Ormel Property Development' Business Card

Business Card Features:

High Quality (potentially textured) thick card - preference is white textured card

Logo (supplied)

We plan to use the vertical logo as the main logo. But i am happy for people to use either if they find it works better for the design of the card.

The building icon and also the insert to the 'E' is in a metallic finish, i think this should be finished in a metallic embossed or raised style.
Updates

Please note i have attached both a horizontal and Vertical Logo for your reference. We plan to use the vertical logo as the main logo. But i am happy for people to use either if they find it works better for the design of the card.

Please note i am considering having the cards made on stainless steel. This introduces the option of having cut outs in the card and etching or printing for the design. If you have a good concept for this please submit.

http://www.tinquarry.example/black-metal-cards# this is a site that makes the metal cards to offer some direction . . . . Please note i am basic the selection o the best design, if that means normal print cards on paper then this is what i will choose. But there are some great options with the metal. Thanks.

Industry/Entity Type

Building

Requirements
Must have
• Helvetica font to details side of card - logo as supplied to opposite side.

Card Details:

Darrow Pketts
Managing Director

+61 487 263 518
+61 3 6172 4809

PO Box 73
Bentleigh, VIC 3024

darrow@ormel.example

www.ormel.example

```html
<!DOCTYPE html>
<html lang="en">
<head>
<meta charset="utf-8">
<title>Ormel Property Development – Business Card</title>
<link href="https://fonts.googleapis.com/css2?family=Open+Sans:wght@400;600;700&display=swap" rel="stylesheet">
<style>
  :root {
    --bg: #d9dadb;
    --card: #ffffff;
    --ink: #5a5c5d;
    --ink-soft: #8b8d8e;
    --band: #5b5e5f;
    --band-light: #b9bbbc;
    --rule: #c9cacb;
    --white: #ffffff;
  }
  * { box-sizing: border-box; margin: 0; padding: 0; }
  html, body {
    width: 1200px; height: 960px; overflow: hidden;
    background: var(--bg);
    font-family: "Open Sans", Helvetica, Arial, sans-serif;
  }
  .card {
    position: absolute; left: 220px;
    width: 760px; height: 430px;
    background: var(--card);
    border-radius: 36px;
    overflow: hidden;
    box-shadow: 0 6px 18px rgba(0,0,0,.18);
  }
  .card--front { top: 25px; }
  .card--back { top: 505px; }

  .wordmark { display: flex; align-items: center; gap: 22px; color: var(--ink); }
  .wordmark__square { width: 70px; height: 70px; background: var(--band-light); }
  .wordmark__divider { width: 1px; height: 110px; background: var(--rule); }
  .wordmark__text { font-weight: 600; line-height: 1; }
  .wordmark__name { font-size: 74px; letter-spacing: 2px; }
  .wordmark__tag { font-size: 17px; letter-spacing: .5px; margin-top: 6px; }

  .card--front .wordmark { position: absolute; left: 170px; top: 105px; }
  .front__url {
    position: absolute; left: 0; right: 0; top: 300px; text-align: center;
    font-size: 21px; letter-spacing: 3px; color: var(--ink);
  }

  .back__band { position: absolute; inset: 0; }
  .back__person {
    position: absolute; right: 36px; top: 100px; text-align: right; color: var(--white);
  }
  .back__name { font-size: 24px; font-weight: 700; }
  .back__role { font-size: 19px; }

  .card--back .wordmark { position: absolute; left: 40px; top: 100px; gap: 16px; }
  .card--back .wordmark__square { width: 54px; height: 54px; }
  .card--back .wordmark__divider { height: 84px; }
  .card--back .wordmark__name { font-size: 56px; }
  .card--back .wordmark__tag { font-size: 13px; }

  .contacts {
    position: absolute; left: 40px; top: 252px; list-style: none;
    font-size: 17px; color: var(--ink-soft);
  }
  .contacts li { display: flex; align-items: center; gap: 10px; height: 27px; }
  .icon { width: 16px; height: 16px; fill: var(--ink); flex: none; }

  .back__divider {
    position: absolute; left: 350px; top: 330px; width: 1px; height: 60px; background: var(--rule);
  }
  .address {
    position: absolute; left: 400px; top: 330px; display: flex; gap: 10px;
    font-style: normal; font-size: 18px; line-height: 1.3; color: var(--ink-soft);
  }
  .address .icon { width: 16px; height: 20px; margin-top: 2px; }
</style>
</head>
<body>

<section class="card card--front" aria-label="Business card front">
  <div class="wordmark">
    <span class="wordmark__square"></span>
    <span class="wordmark__divider"></span>
    <div class="wordmark__text">
      <div class="wordmark__name">ORMEL</div>
      <div class="wordmark__tag">PROPERTY DEVELOPMENT</div>
    </div>
  </div>
  <p class="front__url">www.ormel.example</p>
</section>

<section class="card card--back" aria-label="Business card back">
  <svg class="back__band" viewBox="0 0 760 430" preserveAspectRatio="none" aria-hidden="true">
    <path d="M0 0 H760 V300 C600 200 360 70 0 62 Z" fill="var(--band)"/>
    <path d="M0 74 C360 82 600 212 760 314 V344 C600 234 360 96 0 84 Z" fill="var(--band-light)"/>
  </svg>

  <div class="back__person">
    <div class="back__name">Darrow Pketts</div>
    <div class="back__role">Managing Director</div>
  </div>

  <div class="wordmark">
    <span class="wordmark__square"></span>
    <span class="wordmark__divider"></span>
    <div class="wordmark__text">
      <div class="wordmark__name">ORMEL</div>
      <div class="wordmark__tag">PROPERTY DEVELOPMENT</div>
    </div>
  </div>

  <ul class="contacts">
    <li><svg class="icon" viewBox="0 0 16 16"><circle cx="8" cy="8" r="8"/><path d="M5 4 L7 4 L7.5 6 L6.5 7 Q7.5 9 9 9.5 L10 8.5 L12 9 L12 11 Q7 12 5 4Z" fill="#fff"/></svg>+61 487 263 518</li>
    <li><svg class="icon" viewBox="0 0 16 16"><circle cx="8" cy="8" r="8"/><path d="M5 4 L7 4 L7.5 6 L6.5 7 Q7.5 9 9 9.5 L10 8.5 L12 9 L12 11 Q7 12 5 4Z" fill="#fff"/></svg>+61 3 6172 4809</li>
    <li><svg class="icon" viewBox="0 0 16 16"><rect x="1" y="3" width="14" height="10" rx="1"/><path d="M1.5 4 L8 9 L14.5 4" stroke="#fff" stroke-width="1.4" fill="none"/></svg>darrow@ormel.example</li>
    <li><svg class="icon" viewBox="0 0 16 16"><circle cx="8" cy="8" r="8"/><path d="M1 8 H15 M8 1 V15 M3 4 Q8 6 13 4 M3 12 Q8 10 13 12" stroke="#fff" stroke-width="1" fill="none"/></svg>www.ormel.example</li>
  </ul>

  <span class="back__divider"></span>

  <address class="address">
    <svg class="icon" viewBox="0 0 16 20"><path d="M8 0 A7 7 0 0 1 15 7 C15 12 8 20 8 20 C8 20 1 12 1 7 A7 7 0 0 1 8 0Z"/><circle cx="8" cy="7" r="2.6" fill="#fff"/></svg>
    <span>PO Box 73<br>Bentleigh, VIC 3024</span>
  </address>
</section>

</body>
</html>
```